High end building company who specialise in architecturally designed homes needing a presentation do

We need a document/template that can be used in Indesign. We present proposal's, house plans, specifications at various stages throughout a building project from initial contact right through to completion. We want to have the same feel through out each presentation and be able to use the same first few pages and then be able to insert the contents. Sometimes the content will be A4 and other times when presenting plans will be A3. I have attached an example of one previously used for presenting plans (see 01_Conceptual) and one for proposals (see Proposal Example ). The document needs to have a minimalist look and feel very sophisticated to suit our client base. The look of the document should tie in with our logo design which is also attached.

```html
<!DOCTYPE html>
<html lang="en">
<head>
<meta charset="utf-8">
<title>Outline Brief – Harrowfield Residence</title>
<link href="https://fonts.googleapis.com/css2?family=Figtree:wght@300;400&family=Montserrat:wght@900&display=swap" rel="stylesheet">
<style>
  :root {
    --backdrop: #474546;
    --paper: #ffffff;
    --panel: #333333;
    --accent: #e8541e;
    --ink-light: #ffffff;
    --watermark: #e8e8e8;
  }
  * { margin: 0; padding: 0; box-sizing: border-box; }
  html, body { width: 1200px; height: 1200px; overflow: hidden; }
  body {
    background: var(--backdrop);
    font-family: "Figtree", "Helvetica Neue", Arial, sans-serif;
    position: relative;
  }
  .page {
    position: absolute;
    left: 0; top: 175px;
    width: 1200px; height: 849px;
    background: var(--paper);
    overflow: hidden;
  }
  .page-watermark {
    position: absolute;
    left: 0; top: 0;
    width: 1200px; height: 849px;
  }
  .page-watermark text {
    font-family: "Montserrat", Arial, sans-serif;
    font-weight: 900;
    font-size: 140px;
    fill: var(--watermark);
  }
  .brief-panel {
    position: absolute;
    left: 72px; top: 149px;
    width: 1057px; height: 500px;
    background: var(--panel);
    overflow: hidden;
  }
  .brief-panel .divider {
    position: absolute; left: 0; top: 0;
  }
  .section-label {
    color: var(--accent);
    font-size: 17px;
    font-weight: 400;
    line-height: 21.8px;
    text-transform: uppercase;
  }
  .section-text {
    color: var(--ink-light);
    font-size: 17px;
    font-weight: 400;
    line-height: 21.8px;
  }
  .site-info { position: absolute; left: 37px; top: 305px; }
  .site-info .site-area { margin-top: 22px; }
  .requirements { position: absolute; left: 528px; top: 40px; width: 486px; }
  .requirements ul { list-style: none; }
  .requirements li { display: flex; justify-content: space-between; }
  .requirements .qty { width: 12px; text-align: right; }
  .project-title {
    position: absolute;
    left: 0; width: 1200px;
    top: 696px;
    text-align: center;
    color: var(--accent);
    font-weight: 300;
    font-size: 66px;
    line-height: 1;
    letter-spacing: -0.5px;
  }
</style>
</head>
<body>
  <main class="page">
    <svg class="page-watermark" viewBox="0 0 1200 849" aria-hidden="true">
      <text x="6" y="853" textLength="1276" lengthAdjust="spacingAndGlyphs">OUTLINE BRIEF</text>
    </svg>

    <section class="brief-panel">
      <svg class="divider" width="1057" height="500" viewBox="0 0 1057 500" aria-hidden="true">
        <line x1="177" y1="-2" x2="507" y2="502" stroke="#ffffff" stroke-width="5"/>
      </svg>

      <div class="site-info">
        <div class="location">
          <h2 class="section-label">Location</h2>
          <p class="section-text">184 Ashford Road<br>Belmont<br>QLD 4153</p>
        </div>
        <div class="site-area">
          <h2 class="section-label">Site Area</h2>
          <p class="section-text">10,120m2</p>
        </div>
      </div>

      <div class="requirements">
        <h2 class="section-label">Client Requirements</h2>
        <ul class="section-text">
          <li><span>Bedrooms</span><span class="qty">4</span></li>
          <li><span>Bathrooms</span><span class="qty">2</span></li>
          <li><span>Living Areas</span><span class="qty">2</span></li>
          <li>Outdoor Living Area</li>
          <li>Kitchen</li>
          <li>Study</li>
          <li>Laundry</li>
          <li>Powder Room</li>
          <li>Storage</li>
          <li>Double Garage</li>
          <li>Special Requirements</li>
          <li>Small walk-in wardrobes and study desk to children’s rooms</li>
          <li>Existing Pool to remain</li>
          <li>Existing Jacaranda tree to remain</li>
        </ul>
      </div>
    </section>

    <h1 class="project-title">Harrowfield Residence</h1>
  </main>
</body>
</html>
```